job vacancy cover page

I need to design a one pager for a job I'd like to apply for. The one I have done looks shit and amateur!! Wanting it to look amazing and professional (Not too professional though as they are pretty young and fun).

```html
<!DOCTYPE html>
<html lang="en">
<head>
<meta charset="utf-8">
<title>Why Me? Why Bright Arc?</title>
<link rel="stylesheet" href="https://fonts.googleapis.com/css2?family=Bebas+Neue&family=Carlito:wght@400;700&display=swap">
<style>
  :root {
    --crimson: #c0152f;
    --teal: #1d5e6a;
    --ink: #141414;
    --top-bg: #ebebeb;
    --bottom-bg: #f2f2f2;
    --gold: #f2b632;
  }
  * { box-sizing: border-box; margin: 0; padding: 0; }
  html, body { width: 1200px; height: 675px; overflow: hidden; background: var(--bottom-bg); }
  .page {
    position: relative;
    width: 1200px;
    height: 675px;
    overflow: hidden;
    font-family: "Carlito", "Calibri", sans-serif;
    color: var(--ink);
    background: var(--bottom-bg);
  }
  .top-band { position: absolute; left: 0; top: 0; width: 1200px; height: 366px; background: var(--top-bg); }

  .art { position: absolute; border-radius: 8px; }
  .art-hero { left: 17px; top: 11px; width: 203px; height: 359px;
    background: linear-gradient(160deg, #7a3b1c 0%, #d8263a 35%, #5ac8e8 65%, #f29a1e 100%); opacity: .85; }
  .art-heart { left: 546px; top: 72px; width: 78px; height: 72px; border-radius: 40px;
    background: radial-gradient(circle at 40% 35%, #ff6b6b, #d0101a); }
  .art-trophy { left: 812px; top: 70px; width: 104px; height: 160px;
    background: linear-gradient(180deg, #f7d24a 0%, #d99a12 70%, #7a2a12 100%); }
  .art-star { left: 146px; top: 505px; width: 92px; height: 88px;
    background: radial-gradient(circle, #f8dc7a, #c99524); border-radius: 12px; }
  .art-jumper { left: 541px; top: 504px; width: 80px; height: 116px;
    background: linear-gradient(180deg, #f0f0f0 0%, #5a5fae 100%); }
  .art-rocket { left: 813px; top: 506px; width: 76px; height: 169px;
    background: linear-gradient(180deg, #e8604a 0%, #4f7fd0 60%, #eef2f8 100%); border-radius: 38px 38px 8px 8px; }

  .display { position: absolute; font-family: "Bebas Neue", "Oswald", sans-serif; line-height: 1; white-space: nowrap; }
  .title-why-me { left: 228px; top: 30px; font-size: 77px; color: var(--crimson); letter-spacing: 2px; }
  .title-superhero { left: 265px; top: 120px; font-size: 42px; color: var(--teal); line-height: 54px; letter-spacing: 1.5px; }
  .title-powers { left: 239px; top: 240px; font-size: 29px; color: var(--crimson); letter-spacing: .9px; }
  .title-company { left: 49px; top: 375px; font-size: 75px; color: var(--crimson); letter-spacing: 3px; }
  .heading { font-size: 31px; color: var(--ink); line-height: 35.5px; letter-spacing: .5px; }
  .h-passion { left: 628px; top: 108px; }
  .h-success { left: 945px; top: 108px; }
  .h-values { left: 256px; top: 476px; }
  .h-offer { left: 623px; top: 476px; }
  .h-projects { left: 886px; top: 476px; }

  .list { position: absolute; list-style: none; font-weight: 700; font-size: 15px; line-height: 18.3px; white-space: nowrap; }
  .list li { position: relative; }
  .list.square li::before {
    content: ""; position: absolute; top: 7px; width: 5px; height: 5px; background: var(--ink);
  }
  .list .light { font-weight: 400; }
  .list.stars li svg { position: absolute; left: 0; top: 4px; width: 10px; height: 10px; }

  .powers { left: 282px; top: 270px; }
  .powers li { padding-left: 33px; }
  .passion { left: 607px; top: 153px; }
  .passion li { padding-left: 22px; }
  .success { left: 926px; top: 188px; }
  .success li { padding-left: 24px; }
  .values { left: 272px; top: 510px; }
  .values li { padding-left: 31px; }
  .offer { left: 639px; top: 518px; }
  .offer li { padding-left: 31px; }
  .projects { left: 901px; top: 518px; }
  .projects li { padding-left: 32px; }
  .list.square li::before { left: 0; }
</style>
</head>
<body>
<main class="page">
  <div class="top-band"></div>

  <div class="art art-hero" role="img" aria-label="Illustration of a caped superhero woman standing with hands on hips"></div>
  <h1 class="display title-why-me">Why me ?</h1>
  <p class="display title-superhero">If I was a<br>superhero</p>
  <h2 class="display title-powers">My super powers would be</h2>
  <ul class="list square powers">
    <li>Proactiveness</li>
    <li>Creativity</li>
    <li>Pride <span class="light">in my work</span></li>
    <li>Organisational skills</li>
  </ul>

  <div class="art art-heart" role="img" aria-label="Red glossy heart illustration"></div>
  <h2 class="display heading h-passion">My passion</h2>
  <ul class="list square passion">
    <li>The development of others<br>and / or their teams.</li>
    <li>Helping people learn and<br>be successful in life and in<br>their careers.</li>
    <li>Exceptional client<br>experiences</li>
  </ul>

  <div class="art art-trophy" role="img" aria-label="Gold trophy cup illustration"></div>
  <h2 class="display heading h-success">Some of my<br>success</h2>
  <ul class="list stars success">
    <li><svg viewBox="0 0 10 10" aria-hidden="true"><polygon points="5,0 6.2,3.6 10,3.7 7,6 8.1,9.7 5,7.5 1.9,9.7 3,6 0,3.7 3.8,3.6" fill="var(--gold)"/></svg>Increased client workshops<br>by 85% across accounts.</li>
    <li><svg viewBox="0 0 10 10" aria-hidden="true"><polygon points="5,0 6.2,3.6 10,3.7 7,6 8.1,9.7 5,7.5 1.9,9.7 3,6 0,3.7 3.8,3.6" fill="var(--gold)"/></svg>Delivered double digit<br>revenue increase.</li>
    <li><svg viewBox="0 0 10 10" aria-hidden="true"><polygon points="5,0 6.2,3.6 10,3.7 7,6 8.1,9.7 5,7.5 1.9,9.7 3,6 0,3.7 3.8,3.6" fill="var(--gold)"/></svg>Re-designed workshops for<br>virtual delivery,<br>maintaining key<br>relationships.</li>
  </ul>

  <h1 class="display title-company">Why Bright Arc ?</h1>

  <div class="art art-star" role="img" aria-label="Gold star illustration"></div>
  <h2 class="display heading h-values">Values that stood out</h2>
  <ul class="list square values">
    <li>Change for the better</li>
    <li>Excellence – not mediocre</li>
    <li>Put your heart into it and give a shit</li>
    <li>Going the extra mile</li>
    <li>Take risks</li>
  </ul>

  <div class="art art-jumper" role="img" aria-label="Illustration of a man in a lab coat jumping for joy"></div>
  <h2 class="display heading h-offer">What you offer</h2>
  <ul class="list square offer">
    <li>Learning &amp; Developing</li>
    <li>Team</li>
    <li>Flexibility</li>
    <li>Fun</li>
  </ul>

  <div class="art art-rocket" role="img" aria-label="Illustration of a rocket launching with a smoke trail"></div>
  <h2 class="display heading h-projects">Interesting projects</h2>
  <ul class="list square projects">
    <li>Corvale - Leadership development and<br>team effectiveness</li>
    <li>Lindmark – Change management for<br>true transformation</li>
    <li>Harlow's – Customer centricity at<br>Australia's most iconic department<br>store</li>
  </ul>
</main>
</body>
</html>
```